Power point template

I would like to ppt template to use for a research project. The key topic of the research project is: A cyber security toolkit to protect the privacy data/infrastructure of the health care industry.This file will be used by the entire research team (approx. 50 person) to communicate internally during their official meeting but also to present the project results at the Varnholt Assembly, Conferences and so on. Therefore, the design should be professional, and official. The fact that the ppt will be used by several person for the same project means that the template should allow the user any time (s)he adds a table to have a particular format. Any time the user adds bullet points, these should have a particular color and shape.About the ppt design, you should use the project logo that I am attaching and of course you may use at the layout colors that matches to this logo. Regarding its structure I am attaching the basic ppt (non-professional), without design. You may notice at the bottom of each slide there is the VA flag and a particular phrase beside. Please use that in your proposal as well. You may find images for the VA flag here: https://varnholt-assembly.example/about-va/emblems/banner_en If you need any further clarifications, please do not hesitate to contact me.

```html
<!DOCTYPE html>
<html lang="en">
<head>
<meta charset="utf-8">
<title>Kestrel research presentation template</title>
<link href="https://fonts.googleapis.com/css2?family=Montserrat:wght@400;600;700&family=Open+Sans:wght@400;600&display=swap" rel="stylesheet">
<style>
:root{
  --teal:#19a59c;
  --teal-dark:#0e7d77;
  --teal-light:#cfeeeb;
  --ink:#2f3a40;
  --muted:#8a959b;
  --line:#d9dfe2;
  --flag:#1f3f9a;
  --red:#d9434b;
  --night:#1c3a63;
  --canvas:#eef1f3;
}
*{box-sizing:border-box;margin:0;padding:0}
html,body{width:811px;height:1200px;overflow:hidden;background:var(--canvas)}
body{font-family:"Open Sans",Arial,sans-serif;color:var(--ink)}
.deck{display:grid;grid-template-columns:repeat(3,257px);grid-auto-rows:142px;gap:7px 12px;padding:7px 8px}
.slide{position:relative;background:#fff;border:1px solid var(--line);overflow:hidden}
.slide h2{position:absolute;left:10px;top:8px;font-family:"Montserrat",Arial,sans-serif;font-size:9px;font-weight:700;color:var(--ink)}
.slide h2 .accent{color:var(--teal)}
.footer{position:absolute;left:0;right:0;bottom:0;height:11px;display:flex;align-items:center;gap:4px;padding:0 6px;border-top:1px solid var(--line);font-size:4.5px;color:var(--muted)}
.flag{width:12px;height:7px;background:var(--flag)}
.page-tab{position:absolute;right:0;top:0;width:6px;height:14px;background:var(--teal)}
.txt{position:absolute;font-size:4.5px;line-height:1.45;color:var(--muted)}
.bar{position:absolute;background:var(--teal)}
.grey{position:absolute;background:var(--line)}
.brand{font-family:"Montserrat",Arial,sans-serif;font-weight:700;color:var(--teal);letter-spacing:1px}
.brand-mark{display:inline-block;width:14px;height:14px;border-radius:50%;background:var(--teal);vertical-align:middle;margin-right:4px}
.bullets{position:absolute;list-style:none;font-size:5px;color:var(--ink)}
.bullets li{margin-bottom:4px;padding-left:8px;position:relative}
.bullets li::before{content:"";position:absolute;left:0;top:1.5px;width:4px;height:4px;background:var(--teal)}
.placeholder{position:absolute}
.big{font-family:"Montserrat",Arial,sans-serif;font-weight:700}
table.data{position:absolute;border-collapse:collapse;font-size:4.5px}
table.data th{background:var(--teal);color:#fff;padding:2px 4px;font-weight:600}
table.data td{padding:2px 4px;border-bottom:1px solid var(--line);color:var(--ink)}
table.data tr:nth-child(even) td{background:#f2f8f8}
svg{position:absolute}
</style>
</head>
<body>
<main class="deck">

<!-- 1 cover -->
<section class="slide">
  <div class="placeholder" role="img" aria-label="Laptop with security padlock over a world map" style="left:0;top:0;width:100%;height:96px;background:linear-gradient(135deg,#1c3a63,#2d6a9a)"></div>
  <div class="txt" style="left:10px;top:22px;font-size:8px;color:#fff;font-family:Montserrat,sans-serif;font-weight:700;line-height:1.2">Cybersecurity toolkit<br>for health care</div>
  <div class="txt" style="left:14px;top:104px;font-size:9px"><span class="brand">KESTREL</span></div>
  <div class="footer"><span class="flag"></span>Supported by the Varnholt Assembly</div>
</section>

<!-- 2 title with panel -->
<section class="slide">
  <div class="bar" style="left:0;top:0;width:100%;height:92px;background:linear-gradient(135deg,var(--teal),var(--teal-dark))"></div>
  <div class="txt" style="left:70px;top:18px;font-size:13px;color:#fff"><span class="brand-mark" style="background:#fff"></span><span class="brand" style="color:#fff">KESTREL</span></div>
  <div class="txt" style="left:70px;top:46px;font-size:5px;color:#fff">Presentation title goes here<br>Speaker name, date</div>
  <div class="footer"><span class="flag"></span>Supported by the Varnholt Assembly</div>
</section>

<!-- 3 buttons -->
<section class="slide">
  <h2>Lorem ipsum <span class="accent">dolor</span></h2><span class="page-tab"></span>
  <div class="bar" style="left:40px;top:50px;width:80px;height:14px;border-radius:3px"></div>
  <div class="grey" style="left:135px;top:50px;width:80px;height:14px;border-radius:3px"></div>
  <div class="bar" style="left:40px;top:75px;width:175px;height:3px"></div>
  <div class="footer"><span class="flag"></span>Supported by the Varnholt Assembly</div>
</section>

<!-- 4 brand + image -->
<section class="slide">
  <div class="txt" style="left:12px;top:10px;font-size:11px"><span class="brand-mark"></span><span class="brand">KESTREL</span></div>
  <div class="placeholder" role="img" aria-label="Shield and laptop security illustration" style="left:12px;top:36px;width:90px;height:56px;background:linear-gradient(135deg,#f3c74b,#1c3a63)"></div>
  <div class="txt" style="left:12px;top:98px;width:100px">Lorem ipsum dolor sit amet, consectetur adipiscing elit sed do.</div>
  <div class="footer"><span class="flag"></span>Supported by the Varnholt Assembly</div>
</section>

<!-- 5 text + image -->
<section class="slide">
  <h2>Lorem ipsum <span class="accent">dolor</span></h2><span class="page-tab"></span>
  <div class="txt" style="left:10px;top:26px;width:100px">Lorem ipsum dolor sit amet, consectetur adipiscing elit, sed do eiusmod tempor incididunt ut labore et dolore magna aliqua. Ut enim ad minim veniam.</div>
  <div class="placeholder" role="img" aria-label="Team working with computers" style="left:125px;top:26px;width:120px;height:70px;background:linear-gradient(135deg,#9fd8d3,#4a7f95)"></div>
  <div class="footer"><span class="flag"></span>Supported by the Varnholt Assembly</div>
</section>

<!-- 6 bullets -->
<section class="slide">
  <h2>Lorem ipsum <span class="accent">dolor</span></h2><span class="page-tab"></span>
  <ul class="bullets" style="left:120px;top:30px">
    <li>Lorem ipsum dolor sit</li><li>Consectetur adipiscing</li><li>Sed do eiusmod tempor</li><li>Ut labore et dolore</li><li>Magna aliqua enim</li>
  </ul>
  <div class="placeholder" role="img" aria-label="Secure data illustration" style="left:12px;top:30px;width:95px;height:65px;background:linear-gradient(135deg,#d8eeec,#8fc9c4)"></div>
  <div class="footer"><span class="flag"></span>Supported by the Varnholt Assembly</div>
</section>

<!-- 7 text + teal box -->
<section class="slide">
  <div class="txt" style="left:10px;top:10px;width:70px">Lorem ipsum dolor sit amet, consectetur adipiscing elit sed do eiusmod.</div>
  <div class="bar" style="left:88px;top:10px;width:70px;height:50px"></div>
  <div class="txt" style="left:92px;top:14px;width:62px;color:#fff">Tempor incididunt ut labore et dolore magna.</div>
  <ul class="bullets" style="left:170px;top:12px;font-size:4.5px"><li>Lorem ipsum</li><li>Dolor sit</li><li>Amet elit</li><li>Sed tempor</li></ul>
  <div class="txt" style="left:10px;top:70px;width:140px">Ut enim ad minim veniam, quis nostrud exercitation ullamco laboris nisi ut aliquip.</div>
  <div class="footer"><span class="flag"></span>Supported by the Varnholt Assembly</div>
</section>

<!-- 8 chevrons -->
<section class="slide">
  <h2>Lorem ipsum <span class="accent">dolor</span></h2><span class="page-tab"></span>
  <svg width="237" height="24" style="left:10px;top:38px">
    <polygon points="0,0 50,0 58,12 50,24 0,24" fill="#0e7d77"/>
    <polygon points="60,0 110,0 118,12 110,24 60,24 68,12" fill="#19a59c"/>
    <polygon points="120,0 170,0 178,12 170,24 120,24 128,12" fill="#0e7d77"/>
    <polygon points="180,0 228,0 236,12 228,24 180,24 188,12" fill="#19a59c"/>
  </svg>
  <div class="txt" style="left:12px;top:72px;width:230px">Lorem ipsum dolor sit amet, consectetur adipiscing elit, sed do eiusmod tempor incididunt ut labore.</div>
  <div class="footer"><span class="flag"></span>Supported by the Varnholt Assembly</div>
</section>

<!-- 9 bars -->
<section class="slide">
  <h2>Lorem ipsum <span class="accent">dolor</span></h2><span class="page-tab"></span>
  <div class="grey" style="left:10px;top:30px;width:235px;height:8px"></div>
  <div class="bar" style="left:60px;top:31px;width:90px;height:6px"></div>
  <div class="grey" style="left:10px;top:46px;width:235px;height:8px"></div>
  <div class="bar" style="left:110px;top:47px;width:70px;height:6px"></div>
  <div class="grey" style="left:10px;top:62px;width:235px;height:8px"></div>
  <div class="bar" style="left:40px;top:63px;width:130px;height:6px"></div>
  <div class="grey" style="left:10px;top:78px;width:235px;height:8px"></div>
  <div class="bar" style="left:150px;top:79px;width:80px;height:6px"></div>
  <div class="footer"><span class="flag"></span>Supported by the Varnholt Assembly</div>
</section>

<!-- 10 teal header -->
<section class="slide">
  <div class="bar" style="left:0;top:0;width:100%;height:26px"></div>
  <h2 style="color:#fff">Lorem ipsum dolor</h2>
  <svg width="14" height="14" style="left:14px;top:40px"><circle cx="7" cy="7" r="7" fill="#8a959b"/></svg>
  <div class="txt" style="left:34px;top:40px;width:90px">Lorem ipsum dolor sit amet consectetur.</div>
  <svg width="14" height="14" style="left:14px;top:66px"><circle cx="7" cy="7" r="7" fill="#8a959b"/></svg>
  <div class="txt" style="left:34px;top:66px;width:90px">Sed do eiusmod tempor incididunt.</div>
  <div class="txt" style="left:140px;top:40px;width:100px">Ut labore et dolore magna aliqua ut enim ad minim.</div>
  <div class="footer"><span class="flag"></span>Supported by the Varnholt Assembly</div>
</section>

<!-- 11 central icon -->
<section class="slide">
  <h2>Lorem ipsum <span class="accent">dolor</span></h2><span class="page-tab"></span>
  <svg width="30" height="38" style="left:113px;top:40px"><circle cx="15" cy="14" r="13" fill="#19a59c"/><rect x="9" y="27" width="12" height="8" rx="2" fill="#0e7d77"/></svg>
  <div class="bar" style="left:30px;top:38px;width:60px;height:14px"></div>
  <div class="bar" style="left:30px;top:62px;width:60px;height:14px;background:var(--teal-dark)"></div>
  <div class="bar" style="left:166px;top:38px;width:60px;height:14px;background:var(--teal-dark)"></div>
  <div class="bar" style="left:166px;top:62px;width:60px;height:14px"></div>
  <div class="footer"><span class="flag"></span>Supported by the Varnholt Assembly</div>
</section>

<!-- 12 positive negative -->
<section class="slide">
  <h2>Positive <span class="accent">and</span> <span style="color:var(--red)">negative aspects</span></h2><span class="page-tab"></span>
  <div class="bar" style="left:10px;top:28px;width:112px;height:10px"></div>
  <div class="bar" style="left:134px;top:28px;width:112px;height:10px;background:var(--red)"></div>
  <ul class="bullets" style="left:12px;top:44px;font-size:4.5px"><li>Lorem ipsum dolor</li><li>Sit amet elit</li><li>Sed do eiusmod</li><li>Tempor labore</li></ul>
  <ul class="bullets" style="left:136px;top:44px;font-size:4.5px"><li>Magna aliqua enim</li><li>Minim veniam</li><li>Quis nostrud</li><li>Ullamco nisi</li></ul>
  <div class="footer"><span class="flag"></span>Supported by the Varnholt Assembly</div>
</section>

<!-- 13 table -->
<section class="slide">
  <h2>Lorem ipsum <span class="accent">dolor</span></h2><span class="page-tab"></span>
  <table class="data" style="left:10px;top:26px;width:237px">
    <tr><th>Item</th><th>Q1</th><th>Q2</th><th>Q3</th><th>Q4</th></tr>
    <tr><td>Lorem</td><td>12</td><td>18</td><td>24</td><td>30</td></tr>
    <tr><td>Ipsum</td><td>09</td><td>14</td><td>21</td><td>27</td></tr>
    <tr><td>Dolor</td><td>15</td><td>19</td><td>22</td><td>25</td></tr>
    <tr><td>Amet</td><td>11</td><td>16</td><td>20</td><td>29</td></tr>
  </table>
  <div class="footer"><span class="flag"></span>Supported by the Varnholt Assembly</div>
</section>

<!-- 14 gantt -->
<section class="slide">
  <h2>Lorem ipsum <span class="accent">dolor</span></h2><span class="page-tab"></span>
  <div class="grey" style="left:10px;top:26px;width:237px;height:8px;background:#6d777c"></div>
  <div class="bar" style="left:60px;top:40px;width:60px;height:6px"></div>
  <div class="bar" style="left:90px;top:52px;width:80px;height:6px;background:var(--teal-dark)"></div>
  <div class="bar" style="left:130px;top:64px;width:70px;height:6px"></div>
  <div class="bar" style="left:170px;top:76px;width:60px;height:6px;background:var(--teal-dark)"></div>
  <div class="txt" style="left:12px;top:39px">Task A<br>Task B<br>Task C<br>Task D</div>
  <div class="footer"><span class="flag"></span>Supported by the Varnholt Assembly</div>
</section>

<!-- 15 line chart -->
<section class="slide">
  <h2>Lorem ipsum <span class="accent">dolor</span></h2><span class="page-tab"></span>
  <div class="big" style="position:absolute;left:10px;top:56px;font-size:10px;color:var(--teal)">57%</div>
  <div class="big" style="position:absolute;left:10px;top:80px;font-size:10px;color:var(--teal-dark)">79%</div>
  <svg width="180" height="70" style="left:62px;top:30px">
    <line x1="0" y1="68" x2="180" y2="68" stroke="#d9dfe2"/>
    <polyline points="0,50 30,30 60,40 90,15 120,35 150,20 180,28" fill="none" stroke="#19a59c" stroke-width="1.5"/>
    <polyline points="0,60 30,52 60,56 90,40 120,48 150,38 180,44" fill="none" stroke="#8a959b" stroke-width="1"/>
  </svg>
  <div class="footer"><span class="flag"></span>Supported by the Varnholt Assembly</div>
</section>

<!-- 16 timeline arrows -->
<section class="slide">
  <h2>Lorem ipsum <span class="accent">dolor</span></h2><span class="page-tab"></span>
  <svg width="237" height="16" style="left:10px;top:46px">
    <polygon points="0,0 52,0 58,8 52,16 0,16" fill="#6d777c"/>
    <polygon points="60,0 112,0 118,8 112,16 60,16" fill="#19a59c"/>
    <polygon points="120,0 172,0 178,8 172,16 120,16" fill="#6d777c"/>
    <polygon points="180,0 230,0 236,8 230,16 180,16" fill="#19a59c"/>
  </svg>
  <div class="txt" style="left:12px;top:70px;width:230px">Lorem ipsum · Dolor sit · Amet elit · Sed tempor</div>
  <div class="footer"><span class="flag"></span>Supported by the Varnholt Assembly</div>
</section>

<!-- 17 timeline dots -->
<section class="slide">
  <h2>Lorem ipsum <span class="accent">dolor</span></h2><span class="page-tab"></span>
  <svg width="237" height="14" style="left:10px;top:58px">
    <line x1="0" y1="7" x2="237" y2="7" stroke="#19a59c" stroke-width="2"/>
    <circle cx="20" cy="7" r="5" fill="#19a59c"/><circle cx="80" cy="7" r="5" fill="#0e7d77"/>
    <circle cx="140" cy="7" r="5" fill="#19a59c"/><circle cx="200" cy="7" r="5" fill="#0e7d77"/>
  </svg>
  <div class="txt" style="left:12px;top:36px;width:230px">2019 · Lorem ipsum &nbsp;&nbsp;&nbsp; 2020 · Dolor sit</div>
  <div class="txt" style="left:12px;top:80px;width:230px">2021 · Amet elit &nbsp;&nbsp;&nbsp; 2022 · Sed tempor</div>
  <div class="footer"><span class="flag"></span>Supported by the Varnholt Assembly</div>
</section>

<!-- 18 teal steps -->
<section class="slide">
  <h2>Lorem ipsum <span class="accent">dolor</span></h2><span class="page-tab"></span>
  <svg width="237" height="50" style="left:10px;top:36px">
    <polygon points="0,0 50,0 58,25 50,50 0,50 8,25" fill="#0e7d77"/>
    <polygon points="60,0 110,0 118,25 110,50 60,50 68,25" fill="#19a59c"/>
    <polygon points="120,0 170,0 178,25 170,50 120,50 128,25" fill="#0e7d77"/>
    <polygon points="180,0 228,0 236,25 228,50 180,50 188,25" fill="#19a59c"/>
  </svg>
  <div class="footer"><span class="flag"></span>Supported by the Varnholt Assembly</div>
</section>

<!-- 19 text + icons -->
<section class="slide">
  <div class="big" style="position:absolute;left:10px;top:10px;width:110px;font-size:8px;color:var(--teal-dark);line-height:1.2">Sed ut perspiciatis, unde omnis iste natus</div>
  <div class="txt" style="left:10px;top:44px;width:110px">Lorem ipsum dolor sit amet, consectetur adipiscing elit sed do eiusmod tempor.</div>
  <svg width="100" height="70" style="left:140px;top:20px">
    <circle cx="18" cy="16" r="12" fill="#19a59c"/><circle cx="62" cy="16" r="12" fill="#0e7d77"/>
    <circle cx="18" cy="52" r="12" fill="#0e7d77"/><circle cx="62" cy="52" r="12" fill="#19a59c"/>
  </svg>
  <div class="footer"><span class="flag"></span>Supported by the Varnholt Assembly</div>
</section>

<!-- 20 number -->
<section class="slide">
  <h2>Sed ut perspiciatis <span class="accent">unde</span></h2><span class="page-tab"></span>
  <svg width="180" height="30" style="left:38px;top:30px">
    <circle cx="20" cy="15" r="12" fill="#19a59c"/><circle cx="90" cy="15" r="14" fill="#0e7d77"/><circle cx="160" cy="15" r="12" fill="#19a59c"/>
  </svg>
  <div class="big" style="position:absolute;left:0;right:0;top:76px;text-align:center;font-size:11px;color:var(--teal-dark)">65,190.00</div>
  <div class="footer"><span class="flag"></span>Supported by the Varnholt Assembly</div>
</section>

<!-- 21 bar chart -->
<section class="slide">
  <h2>Sed ut <span class="accent">perspiciatis</span></h2><span class="page-tab"></span>
  <svg width="150" height="80" style="left:14px;top:30px">
    <line x1="0" y1="78" x2="150" y2="78" stroke="#d9dfe2"/>
    <rect x="8" y="40" width="14" height="38" fill="#19a59c"/><rect x="26" y="55" width="14" height="23" fill="#f3b33d"/>
    <rect x="52" y="25" width="14" height="53" fill="#19a59c"/><rect x="70" y="45" width="14" height="33" fill="#f3b33d"/>
    <rect x="96" y="15" width="14" height="63" fill="#19a59c"/><rect x="114" y="35" width="14" height="43" fill="#f3b33d"/>
  </svg>
  <ul class="bullets" style="left:180px;top:40px;font-size:4.5px"><li>Lorem ipsum</li><li>Dolor sit</li><li>Amet elit</li></ul>
  <div class="footer"><span class="flag"></span>Supported by the Varnholt Assembly</div>
</section>

<!-- 22 text + image -->
<section class="slide">
  <div class="big" style="position:absolute;left:10px;top:14px;font-size:8px;color:var(--teal-dark);line-height:1.2">Sed ut perspiciatis<br>unde</div>
  <div class="placeholder" role="img" aria-label="Hospital staff using secure systems" style="left:130px;top:0;width:127px;height:130px;background:linear-gradient(160deg,#cfeeeb,#4a7f95)"></div>
  <div class="txt" style="left:10px;top:46px;width:110px">Lorem ipsum dolor sit amet, consectetur adipiscing elit sed do eiusmod.</div>
  <div class="footer" style="right:127px"><span class="flag"></span>Varnholt Assembly</div>
</section>

<!-- 23 people stats -->
<section class="slide">
  <h2 style="left:0;right:0;text-align:center">Lorem ipsum <span class="accent">dolor sit amet</span></h2><span class="page-tab"></span>
  <div class="bar" style="left:30px;top:38px;width:120px;height:10px;background:#f3b33d"></div>
  <div class="big" style="position:absolute;left:160px;top:36px;font-size:8px;color:#f3b33d">80 pers</div>
  <div class="bar" style="left:30px;top:58px;width:90px;height:10px"></div>
  <div class="big" style="position:absolute;left:160px;top:56px;font-size:8px;color:var(--teal)">60 pers</div>
  <div class="bar" style="left:30px;top:78px;width:60px;height:10px;background:#6d777c"></div>
  <div class="big" style="position:absolute;left:160px;top:76px;font-size:8px;color:#6d777c">40 pers</div>
  <div class="footer"><span class="flag"></span>Supported by the Varnholt Assembly</div>
</section>

<!-- 24 thank you -->
<section class="slide">
  <div class="bar" style="left:0;top:0;width:90px;height:130px"></div>
  <div class="txt" style="left:10px;top:50px;font-size:9px"><span class="brand" style="color:#fff">KESTREL</span></div>
  <div class="big" style="position:absolute;left:150px;top:30px;font-size:12px;line-height:1.1">Thank You</div>
  <div class="txt" style="left:150px;top:48px">For your attention</div>
  <svg width="10" height="40" style="left:136px;top:62px">
    <circle cx="5" cy="5" r="4" fill="#19a59c"/><circle cx="5" cy="20" r="4" fill="#19a59c"/><circle cx="5" cy="35" r="4" fill="#19a59c"/>
  </svg>
  <div class="txt" style="left:150px;top:64px;line-height:2.7">info@kestrel.example<br>+00 000 000 000<br>kestrel.example</div>
  <div class="footer"><span class="flag"></span>Supported by the Varnholt Assembly</div>
</section>

</main>
</body>
</html>
```